Business card for law firm

Need business card for new law firm. Think confident, authoritative, conservative, but not stuffy or old-fashioned.

Contact Information for Business Card

Content for card - logo (uploaded), plus the following:

Paul Wexbury (larger font)
Managing Partner (larger font, but not as large as name)
Level 9, 41 Tansy Lane
Sydney NSW 2000
Main Tel 02 7346 2190
Direct Tel 02 6273 4415
Email paul@qvlegal.com.au
www.qvlegal.com.au

Letterhead design should include logo plus:
Level 9, 41 Tansy Lane
Sydney NSW 2000
Tel 02 6273 4415
www.qvlegal.com.au

```html
<!DOCTYPE html>
<html lang="en">
<head>
<meta charset="utf-8">
<title>Quinvale Lawyers – Business Card</title>
<link rel="stylesheet" href="https://fonts.googleapis.com/css2?family=Cinzel:wght@400&family=Montserrat:wght@400&display=swap">
<style>
  :root {
    --navy: #1a2152;
    --paper: #f8f8fa;
    --ink: #111111;
    --body: #3a3a3f;
    --backdrop: #e3e1db;
    --white: #f4f4f6;
  }
  * { margin: 0; padding: 0; box-sizing: border-box; }
  html, body { width: 1200px; height: 1200px; overflow: hidden; }
  body { background: var(--backdrop); position: relative; font-family: "Montserrat", sans-serif; }

  .card { position: absolute; box-shadow: 2px 3px 6px rgba(0,0,0,0.28); }

  .card--front {
    left: 128px; top: 308px; width: 334px; height: 582px;
    background: var(--paper); text-align: center;
  }
  .card--back {
    left: 489px; top: 558px; width: 582px; height: 333px;
    background: var(--navy); text-align: center;
  }

  .brand-square { position: absolute; left: 50%; transform: translateX(-50%); }
  .card--front .brand-square { top: 400px; }
  .card--front .brand-square { top: 96px; width: 46px; height: 46px; background: var(--navy); }
  .card--back .brand-square { top: 78px; width: 56px; height: 56px; background: var(--white); }

  .wordmark { position: absolute; left: 0; right: 0; font-family: "Cinzel", serif; font-weight: 400; line-height: 1; }
  .card--front .wordmark { top: 182px; color: var(--ink); }
  .card--back .wordmark { top: 186px; color: var(--white); }
  .wordmark__name { display: block; }
  .card--front .wordmark__name { font-size: 36px; }
  .card--back .wordmark__name { font-size: 48px; }
  .wordmark__sub { display: block; }
  .card--front .wordmark__sub { font-size: 13px; letter-spacing: 1.05em; margin-top: 10px; padding-left: 1.05em; }
  .card--back .wordmark__sub { font-size: 17px; letter-spacing: 1.45em; margin-top: 14px; padding-left: 1.45em; }

  .person { position: absolute; left: 0; right: 0; top: 287px; }
  .person__name { font-family: "Cinzel", serif; font-size: 25px; color: var(--navy); line-height: 1; letter-spacing: 0.01em; }
  .person__title { font-size: 16px; color: var(--body); margin-top: 6px; }

  .address { position: absolute; left: 0; right: 0; top: 355px; font-size: 16px; line-height: 21px; color: var(--body); font-style: normal; }

  .contacts { position: absolute; left: 80px; top: 408px; list-style: none; text-align: left; }
  .contacts li { display: flex; align-items: center; height: 25.5px; font-size: 16px; color: var(--body); }
  .contacts svg { width: 14px; height: 14px; margin-right: 6px; fill: var(--navy); flex: none; }
</style>
</head>
<body>

<section class="card card--front" aria-label="Business card front">
  <div class="brand-square"></div>
  <div class="wordmark">
    <span class="wordmark__name">QUINVALE</span>
    <span class="wordmark__sub">LAWYERS</span>
  </div>
  <div class="person">
    <h1 class="person__name">PAUL WEXBURY</h1>
    <p class="person__title">Managing Partner</p>
  </div>
  <address class="address">Level 9, 41 Tansy Lane<br>Sydney NSW 2000</address>
  <ul class="contacts">
    <li><svg viewBox="0 0 16 16" aria-hidden="true"><path d="M1 6c0-3 3-4 7-4s7 1 7 4l-3 1-1-2H5L4 7 1 6zm3 2h8l2 7H2l2-7zm4 1.5a2.5 2.5 0 100 5 2.5 2.5 0 000-5z"/></svg>02 7346 2190</li>
    <li><svg viewBox="0 0 16 16" aria-hidden="true"><path d="M4 0h8a1 1 0 011 1v14a1 1 0 01-1 1H4a1 1 0 01-1-1V1a1 1 0 011-1zm1 2v10h6V2H5zm3 11a1 1 0 100 2 1 1 0 000-2z"/></svg>02 6273 4415</li>
    <li><svg viewBox="0 0 16 16" aria-hidden="true"><path d="M1 3h14v10H1V3zm1.5 1.5v.3L8 9l5.5-4.2v-.3h-11zm0 2.2v4.8L6 8.8 2.5 6.7zm11 0L10 8.8l3.5 2.7V6.7zM7 9.6l-3.6 2.9h9.2L9 9.6 8 10.3 7 9.6z"/></svg>paul@qvlegal.com.au</li>
    <li><svg viewBox="0 0 16 16" aria-hidden="true"><path d="M8 0a8 8 0 110 16A8 8 0 018 0zM5 3C3 4 2 6 2.5 8l2 1 .5 2 1.5 1V9l-2-2 1-2 1.5-.5L7 3H5zm6 1L9.5 5l.5 2 2 1 1.5-1C13.5 5.7 12.5 4.6 11 4z"/></svg>www.qvlegal.com.au</li>
  </ul>
</section>

<section class="card card--back" aria-label="Business card back">
  <div class="brand-square"></div>
  <div class="wordmark">
    <span class="wordmark__name">QUINVALE</span>
    <span class="wordmark__sub">LAWYERS</span>
  </div>
</section>

</body>
</html>
```